Harborline Wealth Marketing Powerpoint

I would like help in creating a cool looking powerpoint to share with prospects in marketing my financial advisory business.

Target Market(s)

High Net Worth Individuals and Families

Industry/Entity Type

Financial Service

Requirements
Must have
• My logo in the presentation.

```html
<!DOCTYPE html>
<html lang="en">
<head>
<meta charset="utf-8">
<title>Harborline Wealth – Marketing Deck</title>
<link href="https://fonts.googleapis.com/css2?family=Roboto:wght@400;500;700&display=swap" rel="stylesheet">
<style>
:root{
  --blue:#0a72c4;
  --blue-dark:#0b5b9e;
  --sky:#6cb8f2;
  --sky-pale:#d6ebfb;
  --graphite:#4a4a4a;
  --ink:#333;
  --mist:#d9d9d9;
  --white:#fff;
}
*{margin:0;padding:0;box-sizing:border-box}
html,body{width:1200px;height:1142px;overflow:hidden;background:var(--mist);font-family:"Roboto",sans-serif;color:var(--ink)}
.deck{position:relative;width:1200px;height:1142px}
.slide{position:absolute;width:377px;height:212px;background:var(--white);overflow:hidden}
.abs{position:absolute}
.footer-bar{position:absolute;left:0;right:0;bottom:0;height:3px;background:var(--blue)}
.page-tab{position:absolute;bottom:0;left:50%;width:20px;height:20px;margin-left:-10px;border-radius:50%;background:var(--blue);transform:translateY(50%);color:#fff;font-size:5px;text-align:center;line-height:10px}
.corner-mark{position:absolute;top:5px;right:6px;font-size:5px;font-weight:700;color:var(--blue);line-height:1}
.brand{font-weight:700;color:var(--blue);line-height:1;white-space:nowrap}
.title{color:var(--blue);font-weight:500;line-height:1.15}
.tiny{font-size:4px;line-height:1.3}
.small{font-size:5px;line-height:1.3}
.photo{position:absolute}
.tick{position:absolute;width:11px;height:11px;border:1px solid var(--blue);border-radius:50%}
.tick::after{content:"";position:absolute;left:3px;top:1.5px;width:3px;height:5px;border-right:1px solid var(--blue);border-bottom:1px solid var(--blue);transform:rotate(40deg)}
.tick.on-dark{border-color:#fff}
.tick.on-dark::after{border-color:#fff}
.piece{position:absolute;width:48px;height:48px;color:#fff;font-size:4.5px;font-weight:500;display:flex;align-items:center;justify-content:center;text-align:center;padding:4px}
.piece.blue{background:var(--blue)}
.piece.dark{background:var(--graphite)}
.piece.light{background:var(--sky)}
.panel{position:absolute;background:var(--blue);color:#fff;text-align:center;padding:6px 6px}
.panel h4{font-size:5.5px;font-weight:500;margin-bottom:4px}
.panel p{font-size:3.8px;line-height:1.35}
.stack-row{height:7px;margin-bottom:2px;background:var(--sky);color:#fff;font-size:3.5px;text-align:center;line-height:7px}
.headline-strip{position:absolute;height:7px;background:#eee;font-size:3.3px;font-weight:700;text-align:right;padding-right:10px;line-height:7px;letter-spacing:.2px}
.plan-col{position:absolute;top:92px;width:50px}
.plan-col h5{font-size:3.6px;font-weight:700;color:var(--graphite);margin-bottom:4px}
.plan-col h6{font-size:3.6px;font-weight:500;color:var(--blue);margin-bottom:3px}
.plan-col p{font-size:3px;line-height:1.4;color:#666}
.rel-item{position:absolute;width:66px}
.rel-item svg{display:block;margin:0 auto 3px}
.rel-item h5{background:var(--blue);color:#fff;font-size:4px;font-weight:500;padding:1px 3px;margin-bottom:3px}
.rel-item p{font-size:3.6px;line-height:1.35;color:#555;padding:0 2px}
.card{position:absolute;top:66px;width:96px;height:120px;background:#fff;box-shadow:0 0 4px rgba(0,0,0,.22);text-align:center;padding:14px 8px 0}
.card .name{font-size:12px;font-weight:700;color:var(--blue);margin-bottom:12px}
.card p{font-size:4.4px;line-height:1.4;color:#333}
.route li{list-style:none;font-size:4.6px;font-weight:500;color:var(--blue);margin-bottom:12px;position:relative;padding-left:10px}
.route li::before{content:"";position:absolute;left:0;top:0;border-left:5px solid var(--blue);border-top:4px solid transparent;border-bottom:4px solid transparent}
.step{position:absolute;color:#fff;font-size:6px;font-weight:500;text-align:center;display:flex;align-items:center;justify-content:center}
.step-edge{position:absolute;background:#e7e7e7}
.contact{position:absolute;width:108px;height:34px;background:var(--graphite);color:#fff;font-size:5.5px;font-weight:500;display:flex;align-items:center}
.contact .icon{width:28px;height:34px;background:var(--blue);display:flex;align-items:center;justify-content:center;margin-right:8px;flex:none}
</style>
</head>
<body>
<main class="deck">

<section class="slide" style="left:19px;top:19px">
  <div class="photo" role="img" aria-label="Misty mountain lake at dawn" style="left:0;top:0;width:377px;height:157px;background:linear-gradient(180deg,#5d5b6c 0%,#8b8896 45%,#b7b6bf 70%,#9a99a4 100%)"></div>
  <div class="brand abs" style="left:0;width:377px;top:75px;text-align:center;font-size:20px">Harborline Wealth</div>
  <div class="title abs" style="left:0;width:377px;top:171px;text-align:center;font-size:18px">Your Slides Deck Name</div>
</section>

<section class="slide" style="left:407px;top:19px;background:#6db2ec">
  <div class="photo" role="img" aria-label="Two hikers standing on a snowy mountain ridge" style="left:0;top:0;width:377px;height:212px;background:linear-gradient(160deg,#cfd6de 0%,#e9edf1 45%,#b9b6b2 75%,#6b625b 100%);clip-path:polygon(0 0,100% 0,100% 100%,58% 100%,0 40%)"></div>
  <svg class="abs" style="left:0;top:0" width="377" height="212" aria-hidden="true">
    <polygon points="0,0 0,80 95,0" fill="#5aa9ea"/>
    <polygon points="310,0 377,0 377,65" fill="#0a72c4"/>
    <polygon points="120,212 215,135 330,212" fill="#3d3d3f"/>
  </svg>
  <div class="brand abs" style="left:0;width:377px;top:58px;text-align:center;font-size:20px">Harborline Wealth</div>
  <div class="abs" style="left:0;width:377px;top:202px;text-align:center;font-size:5px;color:#fff">www.harborlinewealth.com</div>
</section>

<section class="slide" style="left:796px;top:19px">
  <div class="photo" role="img" aria-label="Blue-tinted desk with financial charts and tablet" style="left:0;top:0;width:176px;height:212px;background:linear-gradient(160deg,#1c7fd1 0%,#0b67b6 55%,#0a5a9f 100%)"></div>
  <div class="abs" style="left:8px;width:138px;top:56px;color:#fff;font-size:14px;font-weight:500;text-align:center;line-height:1.25">Harborline Wealth acts with a fiduciary interest to its clients</div>
  <div class="abs" style="left:153px;top:0;width:23px;height:212px;background:var(--blue-dark)"></div>
  <div class="tick on-dark" style="left:159px;top:23px"></div>
  <div class="tick on-dark" style="left:159px;top:48px"></div>
  <div class="tick on-dark" style="left:159px;top:73px"></div>
  <div class="tick on-dark" style="left:159px;top:99px"></div>
  <div class="tick on-dark" style="left:159px;top:124px"></div>
  <div class="tick on-dark" style="left:159px;top:150px"></div>
  <div class="tick on-dark" style="left:159px;top:175px"></div>
  <div class="corner-mark">Harborline Wealth</div>
  <div class="abs small" style="left:180px;top:23px;width:190px;font-size:4.8px">
    <p style="margin-bottom:6px">Providing the highest level of wealth advisory services is at the heart of everything we do.</p>
    <p style="margin-bottom:6px">We love being a trusted advisor to our clients and work hard to cut through all of the noise to deliver exceptional service.</p>
    <p style="margin-bottom:6px">There are so many financial decisions that impact multiple areas of an individual’s balance sheet that focusing on just one or two likely results in a missed opportunity or exposes you to a potentially costly mistake.</p>
    <p style="margin-bottom:6px">Our goal is to give you the piece of mind that all aspects of your financial picture are being taken care of.</p>
    <p style="margin-bottom:6px">As an independent Registered Investment Advisor, we follow the highest financial standard with your best interests as our utmost priority.</p>
    <p style="margin-bottom:6px">We work on a fee-only basis and do not sell commission-based or proprietary products or receive kick-backs of any kind.</p>
    <p>This gives us the freedom to develop your financial plan and investment strategy without biased outside influences.</p>
  </div>
  <div class="footer-bar"></div>
</section>

<section class="slide" style="left:19px;top:242px">
  <div class="corner-mark">Harborline Wealth</div>
  <div class="abs" style="left:114px;top:94px;width:248px;height:46px;background:var(--sky)"></div>
  <div class="piece blue" style="left:16px;top:44px">Investment Management</div>
  <div class="piece dark" style="left:65px;top:44px">Retirement Planning</div>
  <div class="piece blue" style="left:114px;top:44px">Executive Compensation &amp; Benefits</div>
  <div class="piece light" style="left:16px;top:93px">Education</div>
  <div class="piece blue" style="left:65px;top:93px">Insurance</div>
  <div class="piece light" style="left:114px;top:93px">Philanthropy</div>
  <div class="piece blue" style="left:16px;top:142px">Cash Management &amp; Budgeting</div>
  <div class="piece dark" style="left:65px;top:142px">Tax Planning &amp; Compliance</div>
  <div class="piece blue" style="left:114px;top:142px">Estate Planning / Wealth Transfer</div>
  <div class="title abs" style="left:204px;top:63px;font-size:14px">What do we do?</div>
  <div class="abs" style="left:185px;top:105px;width:160px;color:#fff;font-size:5.5px;text-align:center;line-height:1.5">We have the expertise and experience to provide an exceptional personal CFO relationship.</div>
  <div class="footer-bar"></div><div class="page-tab"></div>
</section>

<section class="slide" style="left:407px;top:242px">
  <div class="corner-mark">Harborline Wealth</div>
  <div class="title abs" style="left:28px;top:23px;font-size:11px">Guiding Investment<br>Philosophy</div>
  <div class="tick" style="left:12px;top:69px"></div>
  <div class="abs small" style="left:28px;top:58px;width:178px;font-size:4.6px"><b class="title" style="font-size:5.5px">Embrace Market Pricing</b><br>The market is an effective information-processing machine. Each day, the world equity markets process billions of dollars in trades between buyers and sellers – and the real-time information they bring helps set prices.</div>
  <div class="abs" style="left:0;top:93px;width:180px;height:38px;background:#f2f2f2"></div>
  <div class="tick" style="left:12px;top:110px"></div>
  <div class="abs small" style="left:28px;top:95px;width:178px;font-size:4.6px"><b class="title" style="font-size:5.5px">Don’t Try to Outguess the Market</b><br>The market’s pricing power works against mutual fund managers who try to outperform through stock picking or market timing. As evidence, only 23% of US equity mutual funds and 8% of fixed income funds have survived and outperformed their benchmarks over the past 20 years.</div>
  <div class="tick" style="left:12px;top:163px"></div>
  <div class="abs small" style="left:28px;top:147px;width:178px;font-size:4.6px"><b class="title" style="font-size:5.5px">Resist Chasing Past Performance</b><br>Some investors select mutual funds based on their past returns. Yet, past performance offers little insight into a fund’s future returns. For example, most funds in the top quartile (25%) of previous five-year returns did not maintain a top-quartile ranking in the following five years.</div>
  <svg class="abs" style="left:205px;top:25px" width="165" height="40" aria-hidden="true">
    <circle cx="20" cy="20" r="17" fill="#fff" stroke="#ddd" stroke-width="3"/>
    <circle cx="75" cy="20" r="17" fill="#fff" stroke="#ddd" stroke-width="3"/>
    <circle cx="135" cy="20" r="17" fill="#fff" stroke="#ddd" stroke-width="3"/>
    <path d="M42 14l5 6-5 6M47 14l5 6-5 6M100 14l5 6-5 6M105 14l5 6-5 6" stroke="#0a72c4" stroke-width="2" fill="none"/>
    <text x="20" y="18" font-size="4" text-anchor="middle" fill="#0a72c4">All Available</text>
    <text x="20" y="24" font-size="4" text-anchor="middle" fill="#0a72c4">Information</text>
    <text x="75" y="20" font-size="6" font-weight="700" text-anchor="middle" fill="#0a72c4">$462.8B</text>
    <text x="75" y="26" font-size="2.8" text-anchor="middle" fill="#666">daily trading volume</text>
    <text x="135" y="22" font-size="6" text-anchor="middle" fill="#0a72c4">Prices</text>
  </svg>
  <div class="abs" style="left:216px;top:88px;font-size:4px;font-weight:500">PERCENTAGE OF TOP-RANKED FUNDS THAT STAYED ON TOP</div>
  <div class="abs" style="left:208px;top:97px;width:22px;height:13px;background:var(--blue);color:#fff;font-size:5px;font-weight:700;text-align:center;line-height:1.3">TOP 25 %</div>
  <div class="abs" style="left:208px;top:110px;width:22px;height:62px;background:#e8e8e8"></div>
  <div class="abs" style="left:210px;top:160px;font-size:3.6px;color:#888;text-align:center">Previous<br>5 Years</div>
  <div class="abs" style="left:250px;top:105px;width:90px;height:14px;background:#f0f0f0"></div>
  <div class="abs" style="left:250px;top:105px;width:18px;height:14px;background:var(--sky);color:#fff;font-size:5px;line-height:14px;padding-left:2px">21%</div>
  <div class="abs" style="left:322px;top:110px;font-size:4px;font-weight:500">Equity</div>
  <div class="abs" style="left:250px;top:131px;width:90px;height:14px;background:#f0f0f0"></div>
  <div class="abs" style="left:250px;top:131px;width:24px;height:14px;background:var(--sky);color:#fff;font-size:5px;line-height:14px;padding-left:2px">28%</div>
  <div class="abs" style="left:314px;top:136px;font-size:4px;font-weight:500">Fixed Income</div>
  <div class="abs" style="left:351px;top:136px;font-size:4px">100%</div>
  <svg class="abs" style="left:230px;top:104px" width="20" height="40" aria-hidden="true"><path d="M0 2L20 8M0 2L20 36" stroke="#0a72c4" stroke-width=".6" stroke-dasharray="1.5 1"/></svg>
  <div class="abs" style="left:250px;top:153px;width:100px;font-size:4px;font-weight:500">Funds Remaining in Top Quartile of Returns in the Following 5-years Period (2008-2018 average)</div>
  <div class="footer-bar"></div><div class="page-tab"></div>
</section>

<section class="slide" style="left:796px;top:242px">
  <div class="corner-mark">Harborline Wealth</div>
  <div class="title abs" style="left:0;width:377px;top:10px;text-align:center;font-size:9.5px">The Power of Efficient Markets</div>
  <div class="panel" style="left:0;top:45px;width:115px;height:78px">
    <h4>Let Markets Work for You</h4>
    <p>The financial markets have rewarded long-term investors. People expect a positive return on the capital they supply, and markets have provided growth of wealth over time.</p>
  </div>
  <div class="abs" style="left:115px;top:41px;width:122px">
    <div class="title" style="font-size:5.5px;text-align:center;margin-bottom:2px">Dimensions of Expected Returns</div>
    <div style="font-size:3px;color:var(--blue);text-align:center;margin-bottom:1px">EQUITIES</div>
    <div class="stack-row">Company Size (Market Capitalization)</div>
    <div class="stack-row">Relative Price (Price/Book Equity)</div>
    <div class="stack-row">Profitability (Operating Profits/Book Equity)</div>
    <div style="font-size:3px;color:var(--blue);text-align:center;margin-bottom:1px">FIXED INCOME</div>
    <div class="stack-row">Term (Sensitivity to Interest Rates)</div>
    <div class="stack-row">Credit (Credit Quality of Issuer)</div>
    <div class="stack-row">Currency (Currency of Issuance)</div>
  </div>
  <div class="panel" style="left:237px;top:45px;width:140px;height:78px">
    <h4 style="margin-bottom:1px">Avoid Market Timing</h4>
    <p style="margin-bottom:4px">You never know which market segments will outperform from year to year. By holding a globally diversified portfolio, investors stay positioned for returns.</p>
    <h4 style="margin-bottom:1px">Practice Smart Diversification</h4>
    <p>Holding securities across many market segments can help manage overall risk. Global diversification broadens your investment universe.</p>
  </div>
  <svg class="abs" style="left:4px;top:125px" width="108" height="60" aria-hidden="true">
    <line x1="4" y1="52" x2="104" y2="52" stroke="#999" stroke-width=".4"/>
    <polygon points="4,52 20,44 35,40 50,36 62,28 74,22 84,14 92,12 102,10 102,52" fill="#7fc4b0" opacity=".7"/>
    <polyline points="4,50 20,46 35,42 50,40 62,34 74,30 84,22 92,18 102,14" fill="none" stroke="#0a72c4" stroke-width="1"/>
    <polyline points="4,51 30,48 60,45 90,43 102,41" fill="none" stroke="#7a9a3a" stroke-width=".8"/>
  </svg>
  <div class="abs tiny" style="left:4px;top:124px;font-size:2.8px;color:#666">Growth of a dollar over time</div>
  <div class="abs" style="left:125px;top:134px;width:104px;text-align:center;font-size:3.6px;line-height:1.35"><b style="color:var(--blue)">Consider the Drivers of Returns</b><br>There is a wealth of academic research into what drives returns. Expected returns depend on current market prices and expected future cash flows. Investors can use this information to pursue higher expected returns in their portfolios.</div>
  <svg class="abs" style="left:282px;top:128px" width="85" height="55" aria-hidden="true">
    <g>
      <rect x="0" y="0" width="8" height="8" fill="#2a7a4a"/><rect x="9" y="0" width="8" height="8" fill="#9acb6b"/><rect x="18" y="0" width="8" height="8" fill="#1e5d9c"/><rect x="27" y="0" width="8" height="8" fill="#c7c7c7"/><rect x="36" y="0" width="8" height="8" fill="#7fb7e0"/><rect x="45" y="0" width="8" height="8" fill="#2a7a4a"/><rect x="54" y="0" width="8" height="8" fill="#6e6e6e"/><rect x="63" y="0" width="8" height="8" fill="#9acb6b"/><rect x="72" y="0" width="8" height="8" fill="#1e5d9c"/>
      <rect x="0" y="9" width="8" height="8" fill="#7fb7e0"/><rect x="9" y="9" width="8" height="8" fill="#6e6e6e"/><rect x="18" y="9" width="8" height="8" fill="#9acb6b"/><rect x="27" y="9" width="8" height="8" fill="#2a7a4a"/><rect x="36" y="9" width="8" height="8" fill="#1e5d9c"/><rect x="45" y="9" width="8" height="8" fill="#c7c7c7"/><rect x="54" y="9" width="8" height="8" fill="#7fb7e0"/><rect x="63" y="9" width="8" height="8" fill="#2a7a4a"/><rect x="72" y="9" width="8" height="8" fill="#6e6e6e"/>
      <rect x="0" y="18" width="8" height="8" fill="#1e5d9c"/><rect x="9" y="18" width="8" height="8" fill="#2a7a4a"/><rect x="18" y="18" width="8" height="8" fill="#c7c7c7"/><rect x="27" y="18" width="8" height="8" fill="#7fb7e0"/><rect x="36" y="18" width="8" height="8" fill="#9acb6b"/><rect x="45" y="18" width="8" height="8" fill="#1e5d9c"/><rect x="54" y="18" width="8" height="8" fill="#2a7a4a"/><rect x="63" y="18" width="8" height="8" fill="#c7c7c7"/><rect x="72" y="18" width="8" height="8" fill="#7fb7e0"/>
      <rect x="0" y="27" width="8" height="8" fill="#9acb6b"/><rect x="9" y="27" width="8" height="8" fill="#1e5d9c"/><rect x="18" y="27" width="8" height="8" fill="#6e6e6e"/><rect x="27" y="27" width="8" height="8" fill="#9acb6b"/><rect x="36" y="27" width="8" height="8" fill="#2a7a4a"/><rect x="45" y="27" width="8" height="8" fill="#7fb7e0"/><rect x="54" y="27" width="8" height="8" fill="#c7c7c7"/><rect x="63" y="27" width="8" height="8" fill="#1e5d9c"/><rect x="72" y="27" width="8" height="8" fill="#9acb6b"/>
      <rect x="0" y="36" width="8" height="8" fill="#c7c7c7"/><rect x="9" y="36" width="8" height="8" fill="#7fb7e0"/><rect x="18" y="36" width="8" height="8" fill="#2a7a4a"/><rect x="27" y="36" width="8" height="8" fill="#1e5d9c"/><rect x="36" y="36" width="8" height="8" fill="#6e6e6e"/><rect x="45" y="36" width="8" height="8" fill="#9acb6b"/><rect x="54" y="36" width="8" height="8" fill="#1e5d9c"/><rect x="63" y="36" width="8" height="8" fill="#7fb7e0"/><rect x="72" y="36" width="8" height="8" fill="#2a7a4a"/>
    </g>
  </svg>
  <div class="abs" style="left:258px;top:132px;width:18px;font-size:2.8px;color:#666;line-height:1.6">US Large Cap<br>Intl Value<br>Emerging<br>Small Cap<br>Real Estate<br>Bonds<br>Global Bonds</div>
  <div class="footer-bar"></div><div class="page-tab"></div>
</section>

<section class="slide" style="left:19px;top:465px">
  <div class="corner-mark">Harborline Wealth</div>
  <div class="title abs" style="left:0;width:377px;top:22px;text-align:center;font-size:11px">Behavioral Finance…Beware of Your Emotions</div>
  <div class="panel" style="left:9px;top:46px;width:119px;height:72px;padding-top:12px;background:linear-gradient(160deg,#2a86d4,#0b62ad)">
    <h4 style="font-size:6px">Manage Your Emotions</h4>
    <p>Many people struggle to separate their emotions from investing. Markets go up and down. Reacting to current market conditions may lead to making poor investment decisions.</p>
  </div>
  <ul class="abs" style="left:133px;top:56px;width:110px;list-style:none;font-size:4.4px;line-height:1.35">
    <li>✓ Create an investment plan to fit your needs and risk tolerance</li>
    <li>✓ Structure a portfolio along the dimensions of expected returns</li>
    <li>✓ Diversify globally</li>
    <li>✓ Manage expenses, turnover, and taxes</li>
    <li>✓ Stay disciplined through market dips and swings</li>
  </ul>
  <div class="panel" style="left:247px;top:46px;width:119px;height:72px;padding-top:14px;background:linear-gradient(160deg,#2a86d4,#0b62ad)">
    <h4 style="font-size:5.5px">Look Beyond the Headlines</h4>
    <p>Daily market news and commentary can challenge your investment discipline. Some messages stir anxiety about the future while others tempt you to chase the latest fad. When headlines unsettle you, consider the source and maintain a long-term perspective.</p>
  </div>
  <div class="abs" style="left:9px;top:122px;width:119px;text-align:center;font-size:5px;font-weight:500">Avoid Reactive Investing</div>
  <svg class="abs" style="left:9px;top:130px" width="119" height="60" aria-hidden="true">
    <line x1="0" y1="30" x2="119" y2="30" stroke="#0a72c4" stroke-width=".6"/>
    <polyline points="20,30 40,14 80,48 104,30" fill="none" stroke="#0a72c4" stroke-width="1"/>
    <circle cx="20" cy="30" r="2" fill="#0a72c4"/><circle cx="40" cy="14" r="2" fill="#0a72c4"/><circle cx="80" cy="48" r="2" fill="#0a72c4"/><circle cx="104" cy="30" r="2" fill="#0a72c4"/>
    <text x="8" y="36" font-size="3.2">Optimism</text><text x="33" y="10" font-size="3.2">Elation</text><text x="58" y="29" font-size="3.2">Nervousness</text><text x="76" y="55" font-size="3.2">Fear</text><text x="96" y="26" font-size="3.2">Optimism</text>
  </svg>
  <div class="panel" style="left:128px;top:118px;width:119px;height:72px;padding-top:16px;background:linear-gradient(160deg,#2a86d4,#0b62ad)">
    <h4 style="font-size:5.5px">Focus on What you Can Control</h4>
    <p>A financial advisor can offer expertise and guidance to help you focus on actions that add value. This can lead to a better investment experience.</p>
  </div>
  <div class="headline-strip" style="left:247px;top:122px;width:75px">RETIRE RICH</div>
  <div class="headline-strip" style="left:247px;top:133px;width:119px;padding-right:40px">SELL STOCKS NOW</div>
  <div class="headline-strip" style="left:247px;top:144px;width:80px">THE LOOMING RECESSION</div>
  <div class="headline-strip" style="left:247px;top:155px;width:119px;padding-right:26px">THE TOP 10 FUNDS TO OWN</div>
  <div class="headline-strip" style="left:247px;top:166px;width:75px">MARKET HITS RECORD HIGH</div>
  <div class="headline-strip" style="left:247px;top:177px;width:110px;padding-right:24px">HOUSING MARKET BOOM</div>
  <div class="footer-bar"></div><div class="page-tab">7</div>
</section>

<section class="slide" style="left:407px;top:465px">
  <div class="corner-mark">Harborline Wealth</div>
  <div class="title abs" style="left:0;width:377px;top:12px;text-align:center;font-size:11px">Do you have a plan?</div>
  <div class="abs" style="left:0;top:33px;width:377px;height:18px;background:#1f2630"></div>
  <div class="photo" role="img" aria-label="Row of planning software screenshots" style="left:22px;top:38px;width:330px;height:45px;background:linear-gradient(90deg,#e9edf1,#f7f8fa 30%,#dfe6ee 60%,#f2f4f7)"></div>
  <div class="plan-col" style="left:24px"><h5>DIGITAL ADVICE</h5><h6>A Planning First, Self-Directed Platform</h6><p>• Automated client journeys<br>• A gateway to leveraged execution<br>• Unmatched client experience<br>• Side-by-side management of digital and held assets<br>• Co-developed with partners</p></div>
  <div class="plan-col" style="left:76px"><h5>NEEDS ANALYSIS</h5><h6>Focused, Easy-to-Create Plans</h6><p>• Modules for a variety of common planning needs including:<br>• Asset allocation<br>• Insurance<br>• College planning<br>• Retirement<br>• Income protection and more<br>• Create deliverables in minutes</p></div>
  <div class="plan-col" style="left:128px"><h5>GOAL PLANNER</h5><h6>Interactive Scenario Planning</h6><p>• Compare up to four scenarios<br>• Change values on the fly<br>• Use Monte Carlo or straight-line math<br>• Drive goal-focused conversations</p></div>
  <div class="plan-col" style="left:203px"><h5>DECISION CENTER</h5><h6>Interactive Cash Flow Planning</h6><p>• Open any scenario to see lifetime cash flow<br>• Demonstrate effects of important decisions<br>• Use advanced techniques and what-ifs<br>• Collaboratively build a plan with your clients</p></div>
  <div class="plan-col" style="left:254px"><h5>ADVANCED PLANNING</h5><h6>Complex and Advanced Techniques</h6><p>• Model a wide range of financial scenarios<br>• Create detailed retirement plans<br>• Apply what-if scenarios to plans<br>• Conduct in-depth investment analysis<br>• Leverage comprehensive and flexible tax calculations</p></div>
  <div class="plan-col" style="left:306px"><h5>DISTRIBUTION CENTER</h5><h6>Interactive Estate Planning</h6><p>• Visually tell the story of an estate plan<br>• Show how planning techniques affect the estate<br>• Cover topics like distributions and survivor income<br>• Collaboratively create a distribution plan</p></div>
  <div class="footer-bar"></div><div class="page-tab">8</div>
</section>

<section class="slide" style="left:796px;top:465px">
  <div class="corner-mark">Harborline Wealth</div>
  <div class="photo" role="img" aria-label="City skyline and bridge at dusk in blue tones" style="left:0;top:130px;width:377px;height:82px;background:linear-gradient(180deg,#3c8bd0 0%,#1e68ad 60%,#15548f 100%)"></div>
  <div class="title abs" style="left:16px;top:35px;font-size:16px;font-weight:700">Anywhere, Anytime</div>
  <div class="abs" style="left:198px;top:6px;font-size:3px;font-weight:700;color:var(--blue)">YOUR PERSONAL FINANCIAL WEBSITE</div>
  <div class="abs" style="left:198px;top:13px;font-size:7px;color:#444">Take Control of Your Financial World</div>
  <div class="abs" style="left:198px;top:22px;width:110px;font-size:3px;color:#888">Your financial management website makes it easy to manage your wealth and well-being.</div>
  <div class="photo" role="img" aria-label="Laptop and tablet showing client portal dashboard" style="left:200px;top:36px;width:150px;height:70px;background:linear-gradient(180deg,#f3f5f8,#dde3ea);border:2px solid #333;border-radius:3px"></div>
  <div class="photo" role="img" aria-label="Smartphone showing net worth summary" style="left:14px;top:70px;width:66px;height:124px;background:linear-gradient(180deg,#f4f6f8 0%,#2f8fd6 40%,#5aa84a 75%,#f4f6f8 100%);border:3px solid #222;border-radius:7px"></div>
  <div class="photo" role="img" aria-label="Smartphone showing account list" style="left:87px;top:70px;width:64px;height:124px;background:linear-gradient(180deg,#2f8fd6 0%,#f4f6f8 12%,#eef1f4 100%);border:3px solid #222;border-radius:7px"></div>
  <div class="abs" style="left:175px;top:142px;width:190px;color:#fff;font-size:5.6px;text-align:center;line-height:1.45">More then half of the world’s Web traffic is now coming from mobile phones.<br>You will have a consistent and unified experience across all devices – from a mobile phone, tablet, or personal computer – making it easier then ever to use the Client Portal from wherever you are.</div>
  <div class="abs" style="left:186px;top:203px;font-size:5px;color:#fff">9</div>
</section>

<section class="slide" style="left:19px;top:687px">
  <div class="corner-mark">Harborline Wealth</div>
  <div class="abs" style="left:0;top:0;width:40px;height:212px;background:var(--blue)"></div>
  <div class="abs" style="left:20px;top:106px;transform:translate(-50%,-50%) rotate(-90deg);white-space:nowrap;color:#fff;font-size:9px;font-weight:500">ORGANIZE. MONITOR. COLLABORATE</div>
  <div class="title abs" style="left:40px;width:337px;top:32px;text-align:center;font-size:13px">Harborline Wealth Relationship</div>
  <div class="rel-item" style="left:55px;top:65px">
    <svg width="14" height="14" viewBox="0 0 14 14"><rect x="5" y="0" width="4" height="4" fill="#333"/><rect x="0" y="9" width="4" height="4" fill="#333"/><rect x="5" y="9" width="4" height="4" fill="#333"/><rect x="10" y="9" width="4" height="4" fill="#333"/><path d="M7 4v3M2 9V7h10v2M7 7v2" stroke="#333" fill="none"/></svg>
    <h5>ORGANIZER</h5><p>Connect all your accounts for a consolidated view of your entire financial picture</p></div>
  <div class="rel-item" style="left:128px;top:65px">
    <svg width="14" height="14" viewBox="0 0 14 14"><path d="M1 13h12" stroke="#333"/><rect x="2" y="7" width="2" height="6" fill="#333"/><rect x="5" y="4" width="2" height="9" fill="#333"/><rect x="8" y="6" width="2" height="7" fill="#333"/><rect x="11" y="2" width="2" height="11" fill="#333"/></svg>
    <h5>INVESTMENTS</h5><p>Interactive charts and detailed views help monitor all your accounts.</p></div>
  <div class="rel-item" style="left:202px;top:65px">
    <svg width="16" height="14" viewBox="0 0 16 14"><rect x="4" y="1" width="8" height="7" fill="none" stroke="#333"/><path d="M6 11h4M8 8v3M1 6a6 6 0 0 1 2-4M15 6a6 6 0 0 0-2-4" stroke="#333" fill="none"/></svg>
    <h5>SCREEN SHARING</h5><p>Join a screen sharing session quickly and easily for interactive planning anytime, anywhere.</p></div>
  <div class="rel-item" style="left:275px;top:65px">
    <svg width="14" height="14" viewBox="0 0 14 14"><rect x="1" y="1" width="12" height="12" fill="none" stroke="#333"/><circle cx="7" cy="7" r="3" fill="none" stroke="#333"/></svg>
    <h5>VAULT</h5><p>Safely store your most important financial documents, accessible 24/7.</p></div>
  <div class="rel-item" style="left:55px;top:130px">
    <svg width="14" height="14" viewBox="0 0 14 14"><ellipse cx="7" cy="3" rx="5" ry="2" fill="#333"/><ellipse cx="7" cy="7" rx="5" ry="2" fill="#333"/><ellipse cx="7" cy="11" rx="5" ry="2" fill="#333"/></svg>
    <h5>TRACK SPENDING</h5><p>Know how much you’re spending, and where.</p></div>
  <div class="rel-item" style="left:128px;top:130px">
    <svg width="14" height="14" viewBox="0 0 14 14"><path d="M2 2l10 10M12 2L2 12" stroke="#333" stroke-width="2"/></svg>
    <h5>BUDGETING TOOLS</h5><p>Set budget to help reach your savings goals.</p></div>
  <div class="rel-item" style="left:202px;top:130px">
    <svg width="14" height="14" viewBox="0 0 14 14"><rect x="4" y="0.5" width="6" height="13" rx="1" fill="none" stroke="#333"/><circle cx="7" cy="11" r=".8" fill="#333"/></svg>
    <h5>MOBILE</h5><p>A complete financial picture available on your smart phone.</p></div>
  <div class="rel-item" style="left:275px;top:130px">
    <svg width="14" height="14" viewBox="0 0 14 14"><circle cx="7" cy="7" r="6" fill="none" stroke="#333"/><circle cx="7" cy="7" r="3.5" fill="none" stroke="#333"/><circle cx="7" cy="7" r="1.2" fill="#333"/></svg>
    <h5>GOALS</h5><p>See if you’re on target to reach your most important goals.</p></div>
  <div class="footer-bar"></div><div class="page-tab">10</div>
</section>

<section class="slide" style="left:407px;top:687px">
  <div class="corner-mark">Harborline Wealth</div>
  <div class="title abs" style="left:0;width:377px;top:13px;text-align:center;font-size:13.5px">Top Tier Technology to Bring Best in<br>Class Service</div>
  <div class="card" style="left:31px"><div class="name">Trendgrid</div><p>Trendgrid is the firm’s principal research platform that can deliver institutional level equity and fixed income coverage of 42,000 equities, mutual funds and ETFs in addition to 400,000 economic tools and indicators.</p></div>
  <div class="card" style="left:142px"><div class="name">Ledgerleaf</div><p>Ledgerleaf is an advanced financial management platform that allows clients to track and monitor all of their investments and liquid wealth in one place, including live reporting on balances, performance, asset allocation, asset location and detailed holding information.</p></div>
  <div class="card" style="left:253px"><div class="name">Summit Tax</div><p>Tax software used by the majority of the nation’s top tax firms and businesses for an integrated tax and accounting solution to deliver exceptional tax preparation service to achieve solutions designed to minimize a client’s income, gift and estate taxes.</p></div>
  <div class="footer-bar"></div><div class="page-tab">11</div>
</section>

<section class="slide" style="left:796px;top:687px">
  <div class="corner-mark">Harborline Wealth</div>
  <div class="title abs" style="left:12px;top:18px;font-size:13.5px;font-weight:500">Our Process to Becoming<br>Your Personal CFO</div>
  <div class="brand abs" style="left:218px;top:30px;font-size:12px">Harborline Wealth</div>
  <div class="abs" style="left:0;top:80px;width:108px;height:112px;background:#fff;box-shadow:0 0 4px rgba(0,0,0,.18)"></div>
  <ul class="route abs" style="left:2px;top:87px;width:104px">
    <li>IMAGINE</li>
    <li>TAKING A TRIP</li>
    <li>WITHOUT DIRECTIONS</li>
    <li>YOU MIGHT MAKE IT TO YOUR DESTINATION</li>
    <li style="font-style:italic">BUT DID YOU TAKE THE BEST ROUTE?</li>
  </ul>
  <div class="step-edge" style="left:150px;top:173px;width:220px;height:39px"></div>
  <div class="step-edge" style="left:170px;top:146px;width:182px;height:27px"></div>
  <div class="step-edge" style="left:186px;top:120px;width:148px;height:26px"></div>
  <div class="step-edge" style="left:206px;top:96px;width:110px;height:24px"></div>
  <div class="step" style="left:180px;top:177px;width:160px;height:35px;background:#2f8fe0;font-size:7.5px">Establish / Start Relationship</div>
  <div class="step" style="left:195px;top:149px;width:127px;height:24px;background:#1a8fe0">Gather Info &amp; Analyze</div>
  <div class="step" style="left:205px;top:123px;width:107px;height:23px;background:#13b4e6">Develop Plan / Recs</div>
  <div class="step" style="left:213px;top:99px;width:91px;height:21px;background:#6cb8f2">Implement</div>
  <div class="step" style="left:222px;top:59px;width:73px;height:37px;background:#0a86dc;font-size:5.5px;line-height:1.3">Ongoing Monitoring &amp; Proactive Financial Guidance</div>
  <div class="footer-bar" style="right:200px"></div>
  <div class="abs" style="left:184px;top:203px;font-size:5px;color:#fff">12</div>
</section>

<section class="slide" style="left:407px;top:910px">
  <div class="corner-mark">Harborline Wealth</div>
  <div class="photo" role="img" aria-label="Business people silhouetted against an office window in blue tones" style="left:23px;top:0;width:117px;height:212px;background:linear-gradient(180deg,#2a6aa6 0%,#3b7cb8 40%,#1f5387 100%)"></div>
  <div class="abs" style="left:31px;top:57px;width:135px;height:24px;background:#fff;color:var(--blue);font-size:15px;font-weight:700;text-align:center;line-height:24px">THANK YOU</div>
  <div class="brand abs" style="left:172px;top:48px;width:170px;text-align:center;font-size:18px">Harborline Wealth</div>
  <div class="contact" style="left:144px;top:112px">
    <span class="icon"><svg width="12" height="12" viewBox="0 0 24 24" aria-hidden="true"><path fill="#fff" d="M6.6 10.8a15 15 0 0 0 6.6 6.6l2.2-2.2a1 1 0 0 1 1-.25 11.4 11.4 0 0 0 3.6.57 1 1 0 0 1 1 1V20a1 1 0 0 1-1 1A17 17 0 0 1 3 4a1 1 0 0 1 1-1h3.5a1 1 0 0 1 1 1c0 1.25.2 2.45.57 3.57a1 1 0 0 1-.25 1z"/></svg></span>555 014 2090</div>
  <div class="contact" style="left:261px;top:112px">
    <span class="icon"><svg width="12" height="12" viewBox="0 0 24 24" aria-hidden="true"><rect x="6" y="2" width="12" height="6" fill="#fff"/><rect x="2" y="9" width="20" height="8" rx="1" fill="#fff"/><rect x="6" y="14" width="12" height="8" fill="#fff" stroke="#0a72c4"/></svg></span>555 014 6205</div>
  <div class="contact" style="left:144px;top:154px;font-size:4.6px;line-height:1.35">
    <span class="icon"><svg width="10" height="13" viewBox="0 0 20 26" aria-hidden="true"><path fill="#fff" d="M10 0a9 9 0 0 0-9 9c0 7 9 17 9 17s9-10 9-17a9 9 0 0 0-9-9zm0 12.5A3.5 3.5 0 1 1 10 5.5a3.5 3.5 0 0 1 0 7z"/></svg></span>480 Harbor Avenue, Suite 200<br>Portland, OR 97201</div>
  <div class="contact" style="left:261px;top:154px;font-size:4.8px">
    <span class="icon"><svg width="13" height="13" viewBox="0 0 24 24" aria-hidden="true"><g fill="none" stroke="#fff" stroke-width="1.5"><circle cx="12" cy="12" r="10"/><ellipse cx="12" cy="12" rx="4.5" ry="10"/><path d="M2 12h20M4 6.5h16M4 17.5h16"/></g></svg></span>www.harborlinewealth.com</div>
  <div class="footer-bar"></div><div class="page-tab">13</div>
</section>

</main>
</body>
</html>
```